Business Card Design Project

Hi
I'm currently getting a logo designed which will go on the front. It is designed for s
Fitness instructor/ personal training business.
On the back I would like written:
Boxing for Fitness
Aqua Fitness Professional
PersonalisedTraining 1/1 or Small Group outdoor training
Fun and unique workouts
Weight loss/ Strength training

Also I need on there my details
minaharper27@quillbox.net
0427 395 108
FB Mina Motion

Reason: I would like to extend the deadline to give extra days after I have confirmed the logo in two days

Target Market(s)

Mostly women aged between 20-50

Industry/Entity Type

Training

Font styles to use
Sans Serif

Requirements
Must have
• My logo ( I have attached my favourite logo options )
My details

```html
<!DOCTYPE html>
<html lang="en">
<head>
<meta charset="UTF-8">
<title>Mina Motion – Business Cards</title>
<link rel="stylesheet" href="https://fonts.googleapis.com/css2?family=Questrial&display=swap">
<style>
  :root {
    --backdrop: #d9d9d7;
    --card: #0b0b0b;
    --lime: #7cbf3a;
    --magenta: #d6187f;
    --text: #e6e6e6;
  }
  * { margin: 0; padding: 0; box-sizing: border-box; }
  html, body {
    width: 1200px;
    height: 976px;
    overflow: hidden;
    background: var(--backdrop);
  }
  .canvas {
    position: relative;
    width: 1200px;
    height: 976px;
    display: flex;
    align-items: center;
    justify-content: center;
    gap: 40px;
    font-family: "Questrial", "Century Gothic", sans-serif;
  }
  .card {
    position: relative;
    width: 540px;
    height: 310px;
    background: var(--card);
    box-shadow: 0 6px 18px rgba(0, 0, 0, 0.25);
  }

  /* Front */
  .card-front {
    display: flex;
    align-items: center;
    justify-content: center;
  }
  .brand {
    display: flex;
    align-items: center;
    gap: 18px;
  }
  .brand-dot {
    width: 46px;
    height: 46px;
    border-radius: 50%;
    background: var(--lime);
  }
  .brand-name {
    color: var(--lime);
    font-size: 58px;
    font-weight: 400;
    letter-spacing: 1px;
  }

  /* Back */
  .card-back {
    padding: 34px 40px 0;
  }
  .services {
    list-style: none;
    text-align: center;
    color: var(--text);
    font-size: 12.5px;
    line-height: 1.55;
    margin-left: 110px;
  }
  .footwear-row {
    display: block;
    width: 420px;
    height: 44px;
    margin: 14px auto 0;
    background: linear-gradient(90deg, var(--magenta), var(--lime), var(--magenta), var(--lime), var(--magenta));
    opacity: 0.9;
  }
  .contact {
    list-style: none;
    text-align: center;
    color: var(--text);
    font-size: 16px;
    line-height: 1.35;
    margin-top: 16px;
    margin-right: 90px;
  }
</style>
</head>
<body>
  <main class="canvas">
    <section class="card card-front" aria-label="Business card front">
      <div class="brand">
        <span class="brand-dot" aria-hidden="true"></span>
        <span class="brand-name">Mina Motion</span>
      </div>
    </section>

    <section class="card card-back" aria-label="Business card back">
      <ul class="services">
        <li>Boxing for Fitness</li>
        <li>Aqua Fitness Professional</li>
        <li>Fun and unique workouts</li>
        <li>Weight loss/ Strength training</li>
        <li>PersonalisedTraining 1/1</li>
        <li>Small Group outdoor training</li>
      </ul>
      <div class="footwear-row" role="img" aria-label="Row of alternating pink heels and green trainers silhouettes"></div>
      <ul class="contact">
        <li>minaharper27@quillbox.net</li>
        <li>0427 395 108</li>
        <li>FB Mina Motion</li>
      </ul>
    </section>
  </main>
</body>
</html>
```